Stone Over Tide - Stationery Design Project

Hi everyone,

We need a business card and a stationary set designed for a new corporate video production company based in Sydney, 'Stone Over Tide'.

The name refers to the mythological 'phoenix' so we would like to see designs that are appropriate to both the name and to a creative film company. The key thing is, we need to appear fresh and creative while maintaining professionalism.

We would like to stick with dark colors for the basis of the card. One idea that came up was obsidian/volcanic rock with the logo cracking through to reveal lava or something fire like. This is just one idea that has come up, but we are of course open to others and would love to see what people can come up with. Extensive use of flames/fire imagery is not really what we are after.

Also, cinematic as opposed to corporate is preferable.

**** UPDATE ****
When I hand over the card to a prospective client, I want them to feel like they are receiving an obsidian plate with inscriptions in it (ie the phoenix). Looking for something elemental and rigid to contrast and complement the graceful lines of the logo.

Designs we require:
- Business card
(We would like a business card that makes use of some of the more premium business card printing options, such as foil stamping, embossing/debossing, painted edges, spot UV etc. Doesnt have to use all these things, only what you feel works, but we are looking for a business card that stands out and is memorable and these nice touches have that effect. For an example of what is possible, check out "http://www.velvetprintery.net/base/category/business-card-gallery/".)

- Letter head
- With compliments slip
- Display folder

COPMPANY DETAILS:
ABN: 62 738 294 019
Company Address: 7/18-20 Kell St, Marbury NSW 2058
Name: Rex M. Dunleavy
Title: Producer
Contact Number: 0412 539 204
email: rex@stoneovertide.com
website: www.stoneovertide.com

ABOUT THE PHOENIX:
The phoenix is a musical bird from mythology, known for its long fancy tail and small plume on the top of its head. They are elegant and graceful and symbolize immortality, endurance and strength, believed to live for 5 centuries before they were reborn from their ashes.
Updates

Hi everyone,

We have just updated the design brief to include business contact information, website etc. should anyone require it for their designs.

Thanks

Rex

Target Market(s)

Other creative businesses and marketing firms.

Industry/Entity Type

Printing

Requirements
Must have
• Basic printing requirements:
- CMYK colour space
- 300dpi resolution
- Color bleed/crop marks etc to allow for trimming where necessary
- Source files upon handover
Should not have
• Overuse of fire/flame imagery

```html
<!DOCTYPE html>
<html lang="en">
<head>
<meta charset="utf-8">
<title>Stone Over Tide — Stationery</title>
<link rel="stylesheet" href="https://fonts.googleapis.com/css2?family=Jost:wght@400&display=swap">
<style>
  :root {
    --paper: #ffffff;
    --obsidian: #030303;
    --ember: #c4161c;
    --ink: #1a1a1a;
    --shadow: rgba(0, 0, 0, 0.35);
    --text-font: "Jost", sans-serif;
  }
  * { box-sizing: border-box; margin: 0; padding: 0; }
  html, body { width: 1200px; height: 849px; overflow: hidden; background: var(--paper); }
  .stage { position: relative; width: 1200px; height: 849px; font-family: var(--text-font); }

  .backing { position: absolute; background: var(--ember); }
  .sheet { position: absolute; box-shadow: 1px 2px 4px var(--shadow); }
  .sheet--white { background: var(--paper); border: 1px solid #cfcfcf; }
  .sheet--black { background: var(--obsidian); }

  .masthead {
    position: absolute; background: var(--obsidian);
    display: flex; flex-direction: column; align-items: center; justify-content: flex-end;
    color: var(--paper); box-shadow: 0 2px 3px var(--shadow);
  }
  .brand-dot { border-radius: 50%; background: var(--ember); }
  .brand-name { font-weight: 400; white-space: nowrap; text-transform: uppercase; color: var(--paper); }

  .contact-line { position: absolute; color: var(--ink); white-space: nowrap; }
  .contact-line .sep { color: var(--ember); }

  /* business card */
  .card-back { left: 126px; top: 82px; width: 308px; height: 118px; transform: rotate(-11deg); }
  .card { left: 112px; top: 68px; width: 308px; height: 118px; padding-bottom: 9px; }
  .card .brand-dot { width: 34px; height: 34px; margin-bottom: 30px; }
  .card .brand-name { font-size: 14px; letter-spacing: 5.5px; }

  /* letterhead */
  .letter-back { left: 678px; top: 85px; width: 410px; height: 580px; transform: rotate(14deg); }
  .letter { left: 600px; top: 97px; width: 410px; height: 580px; }
  .letter-head { left: 714px; top: 98px; width: 296px; height: 112px; padding-bottom: 8px; }
  .letter-head .brand-dot { width: 34px; height: 34px; margin-bottom: 29px; }
  .letter-head .brand-name { font-size: 14px; letter-spacing: 5.5px; }
  .letter-contact { left: 716px; top: 218px; font-size: 11.5px; letter-spacing: 0.2px; }

  /* presentation folder */
  .folder { left: 55px; top: 327px; width: 342px; height: 479px; }
  .folder-mark {
    position: absolute; left: 0; top: 510px; width: 342px;
    display: flex; flex-direction: column; align-items: center; transform: translate(55px, 0);
  }
  .folder-mark { left: 0; top: 512px; }
  .folder-mark .brand-dot { width: 48px; height: 48px; margin-bottom: 58px; }
  .folder-mark .brand-name { font-size: 18px; letter-spacing: 10px; }

  /* compliments slip */
  .slip-back { left: 343px; top: 304px; width: 373px; height: 187px; transform: rotate(-14deg); }
  .slip { left: 353px; top: 300px; width: 373px; height: 187px; }
  .slip-head { left: 549px; top: 300px; width: 177px; height: 68px; padding-bottom: 5px; }
  .slip-head .brand-dot { width: 20px; height: 20px; margin-bottom: 18px; }
  .slip-head .brand-name { font-size: 8px; letter-spacing: 3px; }
  .slip-contact { left: 550px; top: 373px; font-size: 6.5px; }
</style>
</head>
<body>
<main class="stage">
  <!-- business card -->
  <div class="backing card-back"></div>
  <div class="masthead card">
    <span class="brand-dot"></span>
    <span class="brand-name">Stone Over Tide</span>
  </div>

  <!-- letterhead -->
  <div class="backing letter-back"></div>
  <div class="sheet sheet--white letter"></div>
  <div class="masthead letter-head">
    <span class="brand-dot"></span>
    <span class="brand-name">Stone Over Tide</span>
  </div>
  <p class="contact-line letter-contact">0412 539 204 <span class="sep">&#9679;</span> 7/18-20 Kell St, Marbury NSW 2058</p>

  <!-- presentation folder -->
  <div class="sheet sheet--black folder"></div>
  <div class="folder-mark">
    <span class="brand-dot"></span>
    <span class="brand-name">Stone Over Tide</span>
  </div>

  <!-- compliments slip -->
  <div class="backing slip-back"></div>
  <div class="sheet sheet--white slip"></div>
  <div class="masthead slip-head">
    <span class="brand-dot"></span>
    <span class="brand-name">Stone Over Tide</span>
  </div>
  <p class="contact-line slip-contact">0412 539 204 <span class="sep">&#9679;</span> 7/18-20 Kell St, Marbury NSW 2058</p>
</main>
</body>
</html>
```